Info Graphic about Maple Ridge Restaurant

This info graphic should detail all releavent details about Maple Ridge, such as opening hours, accepted payment methods, home delivery areas etc. please refer attached word document for details.

Also attached a pdf with old info graphic.

IMPORTANT:. Given there is lot of text, I expect the designer to make this interesting. This will be printed in A1 and also A4
Also, I need this in both Portrait and landscape designs.

Industry/Entity Type

Hospitality

Font styles to use
Serif
Sans Serif
Decorative
Script
Other font styles liked:
• I let designer choose

Colors

Designer to choose colors to be used in the design.

Requirements
Must have
• Refer attached word doc
Nice to have
• Refer attached word doc
Should not have
• Refer attached word doc

```html
<!DOCTYPE html>
<html lang="en">
<head>
<meta charset="utf-8">
<title>Maple Ridge Indian Restaurant – Info Sheet</title>
<link href="https://fonts.googleapis.com/css2?family=Roboto+Condensed:ital,wght@0,400;0,700;1,700&display=swap" rel="stylesheet">
<style>
:root{
  --red:#e3262b;
  --deep-red:#c2272d;
  --band-text:#a8281e;
  --yellow:#f6b526;
  --rust:#c45a24;
  --copy:#b4461f;
  --ink:#222;
  --green:#3aaa35;
  --paper:#fbfaf8;
}
*{box-sizing:border-box;margin:0;padding:0}
html,body{width:1200px;height:846px;overflow:hidden;background:var(--paper)}
body{font-family:"Roboto Condensed",sans-serif;color:var(--copy)}
.sheet{position:relative;width:1200px;height:846px;overflow:hidden;background:var(--paper)}
.abs{position:absolute}
.art{position:absolute;border-radius:6px;z-index:1}

/* brand */
.brand-name{left:100px;top:28px;font-size:33px;font-weight:700;color:var(--deep-red);white-space:nowrap}
.brand-dot{left:52px;top:28px;width:36px;height:36px;border-radius:50%;background:var(--deep-red)}
.brand-web{left:172px;top:66px;font-size:23px;color:#8a2a1a}

/* registration */
.map{left:20px;top:100px;width:234px;height:150px;border:6px solid var(--rust);background:linear-gradient(135deg,#eef0f2,#dfe3e6)}
.reg{left:254px;top:104px;width:396px;height:132px;background:var(--rust);color:#fff;padding:12px 14px;font-size:13px;line-height:20px}
.reg h3{font-size:16px;font-weight:400;border-bottom:1px solid #fff;width:190px;padding-bottom:4px;margin-bottom:6px}
.reg .addr{width:200px;line-height:15px;margin-top:4px}
.reg .contact{position:absolute;left:222px;top:78px;line-height:21px}
.reg .contact svg{vertical-align:-2px;margin-right:8px}

/* management */
.mgmt-ribbon{left:682px;top:20px;width:482px;height:58px}
.mgmt-title{left:694px;top:26px;font-size:38px;color:#fff;font-weight:700}
.mgmt{left:682px;top:76px;width:402px;height:184px;background:var(--yellow);padding:10px 12px;color:var(--ink)}
.mgmt .lbl{font-size:13px;font-weight:700}
.mgmt .val{color:var(--red);font-weight:700;line-height:1}
.mgmt .owner{font-size:36px;margin:2px 0 8px}
.mgmt .phone{font-size:38px;margin:2px 0 6px}
.mgmt .mail{font-size:33px}

/* section bands */
.band{position:absolute;background:var(--yellow);color:var(--band-text);font-size:27px;line-height:38px;padding-left:26px;border-radius:0 20px 20px 0;white-space:nowrap}
.band.round{border-radius:20px}

/* hours */
.clock{left:194px;top:261px;width:56px;height:56px;border-radius:50%;background:var(--deep-red);border:3px solid #fff;box-shadow:0 0 0 2px var(--deep-red)}
.hours{left:19px;top:323px;font-size:16px;border-collapse:collapse}
.hours th{font-weight:400;font-size:17px;padding:0 0 6px;text-align:center}
.hours td{padding:3px 0;white-space:nowrap}
.hours td:first-child{width:153px}
.hours td:nth-child(2){width:129px}
.buffet{left:19px;top:406px;width:398px;height:19px;background:var(--yellow);color:var(--red);font-size:14px;line-height:19px;padding-left:3px}

/* lists */
.list{list-style:none;font-size:15px;line-height:22px}
.list li{position:relative;padding-left:14px}
.list li::before{content:"";position:absolute;left:0;top:7px;width:9px;height:9px;border:2px solid var(--green);border-radius:50%}
.list.dark li::before{border-color:#333}
.list.light li::before{border-color:#fff}

.rules{left:24px;top:490px;color:var(--copy)}
.house{left:296px;top:448px;width:88px;height:72px;background:linear-gradient(160deg,var(--yellow),var(--green))}

/* facilities */
.facilities{left:26px;top:558px;width:354px;height:86px;background:var(--yellow);color:var(--ink)}
.facilities h4{color:var(--red);font-weight:400;font-size:19px;text-align:center;border-bottom:1px solid var(--red);margin:2px 12px 0}
.fac-row{display:flex;justify-content:space-between;padding:4px 4px 0}
.fac{width:66px;text-align:center;font-size:10px;line-height:10px;font-weight:700}
.fac-ico{width:28px;height:28px;margin:2px auto 3px;border-radius:50%;background:#1c1c1c}

/* services */
.services{left:26px;top:650px;width:347px;height:136px;background:var(--red);color:#fff;padding:6px 0 0 9px}
.services h4{color:var(--yellow);font-weight:400;font-size:27px;border-bottom:1px solid var(--yellow);width:320px;padding-left:12px;line-height:32px}
.services .cols{display:flex;margin-top:6px}
.services .list{font-size:16px}
.services .col1{width:145px;border-right:1px solid #fff}
.services .col2{padding-left:9px}

/* warning */
.warning{left:0;top:794px;width:373px;height:52px;background:#000;color:#fff;padding:5px 10px 0 68px}
.warning b{font-size:18px;display:block;line-height:19px}
.warning p{font-size:9.5px;line-height:10px}
.warning svg{position:absolute;left:24px;top:8px}

/* book */
.book-title{left:588px;top:274px;font-size:29px;color:var(--band-text);z-index:2;white-space:nowrap}
.table-art{left:468px;top:308px;width:208px;height:100px;background:linear-gradient(180deg,#f0e4c9,#e08a2a)}
.book-copy{left:451px;top:414px;width:320px;font-size:15px;line-height:22px}
.book-copy b{font-weight:700;color:var(--band-text)}

/* order online */
.online{left:430px;top:515px;color:var(--band-text);font-size:16px;line-height:25px;font-weight:700}
.phone-art{left:612px;top:468px;width:156px;height:140px;background:linear-gradient(160deg,#3a3a3a,#f0a070)}

/* byo */
.glass{left:682px;top:616px;width:28px;height:96px;background:linear-gradient(180deg,#c01a22,#eee)}
.byo-copy{left:451px;top:670px;font-size:16px}
.byo-strip{left:442px;top:694px;width:238px;height:20px;background:var(--red);color:var(--yellow);font-style:italic;font-weight:700;font-size:16px;line-height:20px;text-align:center}

/* partners */
.partner{position:absolute;top:774px;height:52px}

/* payment */
.pay-art{left:1044px;top:280px;width:108px;height:48px;background:linear-gradient(120deg,#444,#8fd08a)}
.pay{font-size:18px;color:var(--band-text)}
.pay .row{position:relative;width:138px;height:25px;border-bottom:1px solid var(--yellow);line-height:25px}
.pay .row svg{position:absolute;right:4px;top:5px}
.pay.col2 .row{width:135px}
.surcharge{left:992px;top:409px;font-size:17px;font-style:italic;font-weight:700;color:var(--band-text)}

/* discounts */
.ticket{left:1076px;top:456px;width:100px;height:58px;background:var(--deep-red);transform:rotate(10deg)}
.vouchers{left:830px;top:511px;color:var(--band-text);font-size:15px;line-height:26px}
.vouchers svg{vertical-align:-2px;margin-left:4px}

/* delivery */
.delivery-band{font-size:27px}
.scooter{left:1066px;top:604px;width:96px;height:126px;background:linear-gradient(160deg,#d8332f,#f2f2f2)}
.deliver-intro{left:812px;top:655px;font-size:15px}
.suburbs{display:grid;grid-template-columns:90px 110px;font-size:15.5px;line-height:20px;list-style:none}
.suburbs.abs{left:812px;top:677px;grid-auto-flow:column;grid-template-rows:repeat(7,20px)}
.charges{left:992px;top:732px;width:208px;height:64px;background:var(--red);color:#fff;font-size:18px;line-height:22px;padding:9px 0 0 11px;z-index:2}
</style>
</head>
<body>
<main class="sheet">

  <div class="abs brand-dot"></div>
  <div class="abs brand-name">Maple Ridge Indian Restaurant</div>
  <div class="abs brand-web">www.mapleridge.com.au</div>

  <div class="abs map" role="img" aria-label="Street map showing the restaurant location among nearby shops"></div>
  <section class="abs reg">
    <h3>Registration Details</h3>
    <div>Birchwood House Pty Ltd T/A Maple Ridge Restaurant</div>
    <div>ABN: 48 602 317 905</div>
    <div class="addr">Shop 7-8, 412 Harlow Avenue,<br>Fernvale, WA 6099<br>Australia</div>
    <div class="contact">
      <div><svg width="12" height="12" viewBox="0 0 12 12"><path d="M2 1l3 2-1 2c1 2 2 3 4 4l2-1 2 3-2 1C5 11 1 7 1 3z" fill="#f6b526"/></svg>08 5550 1234</div>
      <div><svg width="12" height="10" viewBox="0 0 12 10"><rect x="0" y="0" width="12" height="10" fill="#f6b526"/><path d="M0 0l6 5 6-5" stroke="#c45a24" fill="none"/></svg>admin@mapleridge.com.au</div>
    </div>
  </section>

  <svg class="abs mgmt-ribbon" viewBox="0 0 482 58"><polygon points="0,0 438,0 482,48 420,58 0,58" fill="#e3262b"/></svg>
  <div class="abs mgmt-title">New Management</div>
  <section class="abs mgmt">
    <div class="lbl">Restaurant Owner:</div>
    <div class="val owner">Rina Castellan</div>
    <div class="lbl">Mobile:</div>
    <div class="val phone">0400555018</div>
    <div class="lbl">Email:</div>
    <div class="val mail">rina@mapleridge.com.au</div>
  </section>

  <div class="band" style="left:0;top:270px;width:208px;height:38px">Opening Hours</div>
  <div class="abs clock" role="img" aria-label="Clock illustration"></div>
  <table class="abs hours">
    <tr><th></th><th>Morning</th><th>Evening</th></tr>
    <tr><td>Monday to Friday</td><td>11:30AM-2:30PM</td><td>5:00PM – 9:00PM</td></tr>
    <tr><td>Saturday and Sunday</td><td>10 :30AM-2:30PM</td><td>5:00PM – 9:00PM</td></tr>
  </table>
  <div class="abs buffet">Dinner Buffet is available only from Mon-Thu from 5:30PM-8:30PM</div>

  <div class="band" style="left:0;top:446px;width:212px;height:37px">House Rules</div>
  <div class="art house" role="img" aria-label="House with a green tick illustration"></div>
  <ul class="abs list rules">
    <li>Prices are inclusive of GST</li>
    <li>Prices are subject to change without notice</li>
    <li>Outside Food and Beverages (except WINE) are not allowed</li>
  </ul>

  <section class="abs facilities">
    <h4>Facilities</h4>
    <div class="fac-row">
      <div class="fac"><div class="fac-ico" role="img" aria-label="Wheelchair icon"></div>Wheel chair access</div>
      <div class="fac"><div class="fac-ico" role="img" aria-label="Toilet icon"></div>Disabled Toilet inside</div>
      <div class="fac"><div class="fac-ico" role="img" aria-label="Baby changer icon"></div>Baby Changer table</div>
      <div class="fac"><div class="fac-ico" role="img" aria-label="High chair icon"></div>High rise tables for babies</div>
      <div class="fac"><div class="fac-ico" role="img" aria-label="Music icon"></div>Music System</div>
    </div>
  </section>

  <section class="abs services">
    <h4>Services</h4>
    <div class="cols">
      <ul class="list light col1"><li>Functions/Parties</li><li>Bulk Cooking</li><li>Catering</li><li>Special Orders</li></ul>
      <ul class="list light col2"><li>Party Orders</li><li>Business Meetings</li><li>Seminars/Presentations</li></ul>
    </div>
  </section>

  <div class="abs warning">
    <svg width="36" height="32" viewBox="0 0 36 32"><polygon points="18,1 35,31 1,31" fill="#fff"/><rect x="16.5" y="10" width="3" height="12" fill="#000"/><rect x="16.5" y="24" width="3" height="3" fill="#000"/></svg>
    <b>WARNING</b>
    <p>Please inform wait staff for any allergies. Food consumed at your own risk.</p>
  </div>

  <div class="art table-art" role="img" aria-label="Dining table with two chairs illustration"></div>
  <div class="abs book-title">Book your Table</div>
  <p class="abs book-copy">Please visit <b>www.mapleridge.com.au</b> to book your table or contact us on <b>08 5550 1234</b></p>

  <div class="band round" style="left:400px;top:470px;width:206px;height:39px;padding-left:36px">Order Online</div>
  <ul class="abs list online">
    <li>www.mapleridge.com.au</li>
    <li>www.platedash.com.au</li>
    <li>www.quickfeast.com.au</li>
    <li>www.homebite.com.au</li>
  </ul>
  <div class="art phone-art" role="img" aria-label="Hand tapping order on a mobile phone illustration"></div>

  <div class="band round" style="left:400px;top:628px;width:324px;height:38px;padding-left:36px">BYO (Bring your own )</div>
  <div class="art glass" role="img" aria-label="Glass of red wine illustration"></div>
  <div class="abs byo-copy">Wine only - Corkage per bottle apply</div>
  <div class="abs byo-strip">Outside Food is not allowed!</div>

  <div class="band round" style="left:400px;top:730px;width:126px;height:39px;padding-left:14px">Partner</div>
  <div class="partner" style="left:400px;width:94px;background:#f7e31b"></div>
  <div class="partner" style="left:506px;width:86px;background:#e3ebf3;border-radius:4px"></div>
  <div class="partner" style="left:628px;width:46px;height:46px;border-radius:50%;background:#6b6b6b;top:777px"></div>
  <div class="partner" style="left:728px;width:46px;height:46px;border-radius:50%;background:#2f8f3a;top:777px"></div>

  <div class="band" style="left:800px;top:282px;width:240px;height:39px">Payment Methods:</div>
  <div class="art pay-art" role="img" aria-label="Hand holding banknotes illustration"></div>
  <div class="abs pay" style="left:828px;top:334px">
    <div class="row">Cash<svg width="20" height="16"><polyline points="2,8 8,14 18,2" stroke="#3aaa35" stroke-width="4" fill="none"/></svg></div>
    <div class="row">DebitLink<svg width="20" height="16"><polyline points="2,8 8,14 18,2" stroke="#3aaa35" stroke-width="4" fill="none"/></svg></div>
    <div class="row">Nova/Meridian<svg width="20" height="16"><polyline points="2,8 8,14 18,2" stroke="#3aaa35" stroke-width="4" fill="none"/></svg></div>
    <div class="row" style="border:0">Debit/Credit<svg width="20" height="16"><polyline points="2,8 8,14 18,2" stroke="#3aaa35" stroke-width="4" fill="none"/></svg></div>
  </div>
  <div class="abs pay col2" style="left:1024px;top:334px">
    <div class="row">Crestline*<svg width="20" height="16"><polyline points="2,8 8,14 18,2" stroke="#3aaa35" stroke-width="4" fill="none"/></svg></div>
    <div class="row">Orient*<svg width="20" height="16"><polyline points="2,8 8,14 18,2" stroke="#3aaa35" stroke-width="4" fill="none"/></svg></div>
    <div class="row" style="border:0">Supper Club<svg width="16" height="16"><path d="M2 2l12 12M14 2L2 14" stroke="#e3262b" stroke-width="4"/></svg></div>
  </div>
  <div class="abs surcharge">*Surcharge of 2.8% apply</div>

  <div class="band round" style="left:810px;top:464px;width:390px;height:40px;border-radius:20px 0 0 20px">Discount Vouchers:</div>
  <div class="art ticket" role="img" aria-label="Discount voucher ticket illustration"></div>
  <ul class="abs list dark vouchers">
    <li>CityPerks Book Vouchers<svg width="20" height="16"><polyline points="2,8 8,14 18,2" stroke="#3aaa35" stroke-width="4" fill="none"/></svg></li>
    <li>Maple Ridge supplied Discount vouchers<svg width="20" height="16"><polyline points="2,8 8,14 18,2" stroke="#3aaa35" stroke-width="4" fill="none"/></svg></li>
    <li>CityPerks Vouchers are eligible only for Dine-In.</li>
  </ul>

  <div class="band round delivery-band" style="left:792px;top:610px;width:408px;height:40px;border-radius:20px 0 0 20px;padding-left:20px">Home/Office Delivery:</div>
  <div class="art scooter" role="img" aria-label="Delivery rider on a red scooter illustration"></div>
  <div class="abs deliver-intro">We deliver to following suburbs</div>
  <ol class="abs suburbs">
    <li>1 Beldon</li><li>2 Craigie</li><li>3 Darch</li><li>4 Duncraig</li><li>5 Edgewater</li><li>6 Greenwood</li><li>7 Hocking</li>
    <li>8 Kingsley</li><li>9 Madeley</li><li>10 Padbury</li><li>11 Pearsall</li><li>12 Wangara</li><li>13 Fernvale</li>
  </ol>
  <div class="abs charges">Delivery Charges $5 and minimum order value $30</div>

</main>
</body>
</html>
```